Postcard Design For House buying

I buy houses for cash that need a lot of repairs and need a post card that illustrate that, i would like one that is somehow cartoonish, I had an idea about a house and a man that was kicking to the house like you do with old cars and then he had some $ bills in his hand. This is just an idea and you should not limit yourself to that

Target Market(s)

Dallas TX (DFW)

Industry/Entity Type

Real Estate

Requirements
Must have
• A Text on the frot calling for action, like "Sell your house fast Call 512-374-9160"

```html
<!DOCTYPE html>
<html lang="en">
<head>
<meta charset="utf-8">
<title>Sell Your House Fast – Postcard</title>
<link rel="stylesheet" href="https://fonts.googleapis.com/css2?family=Cabin:wght@400;500&family=Squada+One&display=swap">
<style>
  :root {
    --paper: #ffffff;
    --edge: #9a9a9a;
    --panel-blue: #8fa6d8;
    --art-light: #a3b6e0;
    --art-dark: #8299cf;
    --navy: #262a63;
    --sun: #fcd20b;
    --ink: #111111;
    --brick: #93282a;
    --cta-yellow: #fcd63a;
    --rule: #222222;
  }
  * { box-sizing: border-box; margin: 0; padding: 0; }
  html, body { width: 1200px; height: 930px; overflow: hidden; background: var(--paper); }
  .postcard {
    position: relative; width: 1200px; height: 930px;
    background: var(--paper); border: 1px solid var(--edge);
  }
  .offer-panel {
    position: absolute; left: 28px; top: 28px; width: 550px; height: 683px;
    background: var(--panel-blue); border-radius: 22px;
  }
  .hero-art {
    position: absolute; left: 14px; top: 14px; width: 522px; height: 316px;
    border-radius: 16px;
    background: radial-gradient(ellipse at 55% 40%, var(--art-light), var(--art-dark) 80%);
  }
  .offer-heading {
    position: absolute; left: 0; right: 0; top: 330px;
    text-align: center; color: var(--navy); white-space: nowrap;
    font-family: "Squada One", sans-serif; font-weight: 400;
    font-size: 58px; line-height: 1; letter-spacing: 2px;
  }
  .benefit-box {
    position: absolute; left: 12px; top: 391px; width: 525px; height: 278px;
    background: var(--sun); border-radius: 18px;
    padding: 20px 0 0 18px; list-style: none;
  }
  .benefit {
    display: flex; align-items: center; gap: 13px; height: 41.7px;
    font-family: "Cabin", sans-serif; font-weight: 500; font-size: 29px;
    color: var(--ink); white-space: nowrap;
  }
  .benefit svg { flex: none; }
  .call-band {
    position: absolute; left: 28px; top: 722px; width: 550px; height: 176px;
    background: var(--brick); border-radius: 20px; color: var(--cta-yellow);
    font-family: "Squada One", sans-serif; text-align: center; overflow: hidden;
  }
  .call-tagline {
    position: absolute; left: 0; right: 0; top: 24px; padding-left: 24px;
    font-size: 54px; line-height: 1; letter-spacing: 2px; white-space: nowrap;
  }
  .call-number {
    position: absolute; left: 14px; right: 0; top: 86px;
    display: flex; align-items: center; justify-content: center; gap: 6px;
    font-size: 80px; line-height: 1; letter-spacing: 3px; white-space: nowrap;
  }
  .call-number svg { flex: none; }
  .stamp-box {
    position: absolute; left: 1041px; top: 47px; width: 115px; height: 142px;
    border: 2px solid var(--rule);
  }
  .address-line { position: absolute; height: 2px; background: var(--rule); right: 45px; }
  .line-1 { top: 469px; left: 646px; }
  .line-2 { top: 553px; left: 646px; }
  .line-3 { top: 637px; left: 646px; }
  .line-4 { top: 721px; left: 900px; }
</style>
</head>
<body>
<main class="postcard">
  <section class="offer-panel">
    <div class="hero-art" role="img" aria-label="Cartoon hand holding cash toward a hand offering house keys, with a speech bubble showing a small yellow house"></div>
    <h1 class="offer-heading">WE BUY HOUSES IN:</h1>
    <ul class="benefit-box">
      <li class="benefit"><svg width="33" height="33" viewBox="0 0 33 33"><rect x="2" y="4" width="26" height="26" rx="3" fill="none" stroke="#111" stroke-width="3.5"/><path d="M7 16l7 7L31 4" fill="none" stroke="#111" stroke-width="4.5" stroke-linejoin="round"/></svg>Any Condition No repair needed</li>
      <li class="benefit"><svg width="33" height="33" viewBox="0 0 33 33"><rect x="2" y="4" width="26" height="26" rx="3" fill="none" stroke="#111" stroke-width="3.5"/><path d="M7 16l7 7L31 4" fill="none" stroke="#111" stroke-width="4.5" stroke-linejoin="round"/></svg>Any Situation</li>
      <li class="benefit"><svg width="33" height="33" viewBox="0 0 33 33"><rect x="2" y="4" width="26" height="26" rx="3" fill="none" stroke="#111" stroke-width="3.5"/><path d="M7 16l7 7L31 4" fill="none" stroke="#111" stroke-width="4.5" stroke-linejoin="round"/></svg>Inherit Nightmare</li>
      <li class="benefit"><svg width="33" height="33" viewBox="0 0 33 33"><rect x="2" y="4" width="26" height="26" rx="3" fill="none" stroke="#111" stroke-width="3.5"/><path d="M7 16l7 7L31 4" fill="none" stroke="#111" stroke-width="4.5" stroke-linejoin="round"/></svg>No commission to be paid</li>
      <li class="benefit"><svg width="33" height="33" viewBox="0 0 33 33"><rect x="2" y="4" width="26" height="26" rx="3" fill="none" stroke="#111" stroke-width="3.5"/><path d="M7 16l7 7L31 4" fill="none" stroke="#111" stroke-width="4.5" stroke-linejoin="round"/></svg>We pay all normal closing cost.</li>
      <li class="benefit"><svg width="33" height="33" viewBox="0 0 33 33"><rect x="2" y="4" width="26" height="26" rx="3" fill="none" stroke="#111" stroke-width="3.5"/><path d="M7 16l7 7L31 4" fill="none" stroke="#111" stroke-width="4.5" stroke-linejoin="round"/></svg>Get a Free Offer</li>
    </ul>
  </section>

  <section class="call-band">
    <p class="call-tagline">SELL YOUR HOUSE FAST</p>
    <p class="call-number">
      <svg width="46" height="46" viewBox="0 0 24 24" aria-hidden="true"><path fill="#fcd63a" d="M6.6 10.8a15.1 15.1 0 006.6 6.6l2.2-2.2c.3-.3.7-.4 1-.2 1.1.4 2.3.6 3.6.6.6 0 1 .4 1 1V20c0 .6-.4 1-1 1A17 17 0 013 4c0-.6.4-1 1-1h3.5c.6 0 1 .4 1 1 0 1.3.2 2.5.6 3.6.1.3 0 .7-.2 1z"/></svg>
      <span>214-555-0173</span>
    </p>
  </section>

  <div class="stamp-box" aria-label="Stamp area"></div>
  <div class="address-line line-1"></div>
  <div class="address-line line-2"></div>
  <div class="address-line line-3"></div>
  <div class="address-line line-4"></div>
</main>
</body>
</html>
```